Van wraps

I need 3 wrap designs to go along with the wrap you already designed. I also have a couple of small changes to that original design. Check the previous conversation for van styles and awareness things for each van.
On the back of the original van design please move the phone number down along the bottom and make bigger. Also change all phone numbers on all designs to 555-817-4926.
Please move the phone number up under the window and change to red.
Remove pink and green boxes. Instead put the pink ribbon on the door and make it say we support breast cancer awareness. On the other side put puppy and kitten on door and say adopt a pet.
Look and feel

```html
<!DOCTYPE html>
<html lang="en">
<head>
<meta charset="utf-8">
<title>Harlow Heating &amp; Air – Van Wrap Sides</title>
<link rel="stylesheet" href="https://fonts.googleapis.com/css2?family=Archivo+Black&family=Nunito:wght@800;900&display=swap">
<style>
  :root {
    --bg: #ffffff;
    --panel-edge: #d9d9d9;
    --wrap-white: #ffffff;
    --blue-deep: #0b4ea8;
    --blue-bright: #2a8ff0;
    --red-deep: #b80d12;
    --red-bright: #e3262b;
    --mark-grey: #7b7b7b;
    --ink: #2b2b2b;
    --outline: #ffffff;
    --pink: #e0459b;
    --orange: #f08a00;
    --pet-warm: #c98a4e;
    --pet-light: #e9d7c2;
  }
  html, body {
    margin: 0;
    width: 1200px;
    height: 1000px;
    overflow: hidden;
    background: var(--bg);
  }
  .wrap-sheet { display: block; width: 1200px; height: 1000px; }
  .panel-base { fill: var(--wrap-white); stroke: var(--panel-edge); stroke-width: 2; }
  .band-blue { fill: url(#blueSweep); }
  .band-red { fill: url(#redSweep); }
  .brand-square { fill: var(--mark-grey); }
  .brand-name { font-family: "Archivo Black", sans-serif; fill: var(--ink); }
  .brand-name--main { font-size: 70px; letter-spacing: 1px; }
  .brand-name--sub { font-size: 24px; }
  .contact {
    font-family: "Nunito", sans-serif;
    font-weight: 900;
    fill: #111;
    stroke: var(--outline);
    stroke-width: 5px;
    paint-order: stroke;
    stroke-linejoin: round;
  }
  .contact--phone { font-size: 30px; letter-spacing: 1px; }
  .contact--web { font-size: 32px; }
  .plate { font-family: "Nunito", sans-serif; font-weight: 900; font-size: 20px; fill: #111; letter-spacing: 1px; }
  .cause { font-family: "Nunito", sans-serif; font-weight: 900; font-size: 13px; }
  .cause--pink { fill: var(--pink); }
  .cause--orange { fill: var(--orange); stroke: #222; stroke-width: 0.6px; paint-order: stroke; }
  .ribbon-area { fill: var(--pink); }
  .pet-area { fill: url(#petTone); }
</style>
</head>
<body>
<svg class="wrap-sheet" viewBox="0 0 1200 1000" xmlns="http://www.w3.org/2000/svg">
  <defs>
    <radialGradient id="blueSweep" cx="0.55" cy="0.2" r="0.8">
      <stop offset="0" stop-color="var(--blue-bright)"/>
      <stop offset="1" stop-color="var(--blue-deep)"/>
    </radialGradient>
    <linearGradient id="redSweep" x1="0" y1="0" x2="0" y2="1">
      <stop offset="0" stop-color="var(--red-bright)"/>
      <stop offset="1" stop-color="var(--red-deep)"/>
    </linearGradient>
    <linearGradient id="petTone" x1="0" y1="0" x2="1" y2="0">
      <stop offset="0" stop-color="var(--pet-warm)"/>
      <stop offset="1" stop-color="var(--pet-light)"/>
    </linearGradient>
  </defs>

  <!-- Driver side -->
  <g class="side side--driver">
    <rect class="panel-base" x="20" y="20" width="1160" height="420" rx="24"/>
    <path class="band-blue" d="M590,21 H1160 A20,20 0 0 1 1179,40 V172 C980,186 830,214 720,252 Z"/>
    <path class="band-red" d="M460,439 C520,335 690,272 860,242 C980,222 1100,208 1179,203 V420 A20,20 0 0 1 1160,439 Z"/>

    <rect class="brand-square" x="540" y="60" width="170" height="170" rx="22"/>
    <text class="brand-name brand-name--main" x="760" y="128">HARLOW</text>
    <text class="brand-name brand-name--sub" x="764" y="160">Heating &amp; Air Conditioning</text>
    <text class="brand-name brand-name--sub" x="890" y="188">Plumbing</text>

    <text class="plate" x="132" y="208">OK 40913</text>

    <rect class="ribbon-area" x="370" y="228" width="36" height="58" rx="6" role="img" aria-label="Pink awareness ribbon"/>
    <text class="cause cause--pink" x="388" y="308" text-anchor="middle">We Proudly Support</text>
    <text class="cause cause--pink" x="388" y="327" text-anchor="middle">Breast Cancer Awareness</text>

    <text class="contact contact--phone" x="830" y="252">555-817-4926</text>
    <text class="contact contact--web" x="555" y="345">harlowair.com</text>
  </g>

  <!-- Passenger side -->
  <g class="side side--passenger" transform="translate(0,500)">
    <rect class="panel-base" x="20" y="20" width="1160" height="420" rx="24"/>
    <g transform="translate(1200,0) scale(-1,1)">
      <path class="band-blue" d="M590,21 H1160 A20,20 0 0 1 1179,40 V172 C980,186 830,214 720,252 Z"/>
      <path class="band-red" d="M460,439 C520,335 690,272 860,242 C980,222 1100,208 1179,203 V420 A20,20 0 0 1 1160,439 Z"/>
    </g>

    <rect class="brand-square" x="490" y="60" width="170" height="170" rx="22"/>
    <text class="brand-name brand-name--main" x="100" y="108">HARLOW</text>
    <text class="brand-name brand-name--sub" x="104" y="140">Heating &amp; Air Conditioning</text>
    <text class="brand-name brand-name--sub" x="200" y="168">Plumbing</text>

    <text class="plate" x="962" y="188">OK 40913</text>

    <rect class="pet-area" x="780" y="205" width="90" height="70" rx="6" role="img" aria-label="Photo of a puppy and a kitten sitting together"/>
    <text class="cause cause--orange" x="805" y="298" text-anchor="middle">We Proudly Support</text>
    <text class="cause cause--orange" x="805" y="318" text-anchor="middle">Pet Adoption</text>

    <text class="contact contact--phone" x="145" y="230">555-817-4926</text>
    <text class="contact contact--web" x="385" y="323">harlowair.com</text>
  </g>
</svg>
</body>
</html>
```